Spa Business Card Design Project

Hello! We are a boutique spa for men and women that is rebranding. I would like a memorable new business card that showcases our beautiful new logo and our unique business. I would like it to be classic/timeless and eclectic/artistic at the  same time.
I am a fan of negative space as you can tell from the logo. I am also open to any creative ideas.
Multi sided design. Two sided design is acceptable as an option, too. "Flaps/folds/whatever the design term is" are optional- whether full vertical or horizontal, half flap, full flap etc
On either side next to the golden snail I would potentially like to see "Breathe deep. Savor Today."  Possibly on one statment on top of each other, crowned with the snail. Or the statment following the snail on one line... I am open for a creative suprise, too.
The back I would like room for the standard Information
"3817 Birch Lane
Marlow, Vermont 05344
(518) 462 3085
info@thecorvella spa.com
The snail is to be done in gold ink.
Can I also Have an option for cards that are individualized for staff members, too?

Updates
Project Deadline Extended
Reason: I apologize for the deadline extension. My day was more involved than anticipated in other matters. Hope to have this closed by next Tuesday.
Thank you

Target Market(s)
Men and women with expendable income between the ages of 30-55
Industry/Entity Type
Boutique
Requirements
Must have
- only black and gold ink.

Nice to have
- One of a kind.
Showcase the snail :-)
make you smile :-)
Fun, but professional.
Should not have
- Lots of color.
Too feminine.
Too busy.

```html
<!DOCTYPE html>
<html lang="en">
<head>
<meta charset="utf-8">
<title>The Corvella Spa — Business Cards</title>
<link rel="stylesheet" href="https://fonts.googleapis.com/css2?family=Cormorant+Garamond:wght@400&family=Open+Sans:wght@400;600&display=swap">
<style>
  :root {
    --backdrop: #2b2b2b;
    --ink-black: #0b0b0b;
    --ink-white: #f2f2f2;
    --gold: #d9a32a;
    --gold-light: #e6b53a;
    --gold-deep: #c48a1e;
    --text-dark: #1a1408;
  }
  * { box-sizing: border-box; margin: 0; padding: 0; }
  html, body {
    width: 833px; height: 1200px; overflow: hidden;
    background: var(--backdrop);
  }
  .sheet {
    position: relative; width: 833px; height: 1200px;
    display: flex; flex-direction: column; align-items: center; justify-content: center; gap: 90px;
  }
  .card {
    position: relative; width: 700px; height: 400px;
    box-shadow: 0 18px 40px rgba(0,0,0,.55);
    overflow: hidden;
  }

  /* Front */
  .card-front { background: var(--ink-black); color: var(--ink-white); }
  .front-web {
    position: absolute; left: 34px; bottom: 30px;
    font-family: "Open Sans", sans-serif; font-size: 14px; letter-spacing: .5px; color: var(--ink-white);
  }
  .front-web .accent { color: var(--gold); }
  .brand {
    position: absolute; left: 0; right: 0; top: 110px; text-align: center;
  }
  .brand-name {
    display: inline-flex; align-items: center; gap: 14px;
    font-family: "Cormorant Garamond", serif; font-weight: 400;
    font-size: 54px; letter-spacing: 4px; color: var(--ink-white); line-height: 1;
  }
  .brand-dot { width: 14px; height: 14px; border-radius: 50%; background: var(--gold); flex: none; }
  .brand-tagline {
    margin-top: 16px;
    font-family: "Open Sans", sans-serif; font-size: 17px; color: var(--ink-white); letter-spacing: .5px;
  }

  /* Back */
  .card-back {
    background: radial-gradient(ellipse at 40% 35%, var(--gold-light) 0%, var(--gold) 55%, var(--gold-deep) 100%);
    color: var(--text-dark);
    font-family: "Open Sans", sans-serif;
  }
  .motto {
    position: absolute; right: 90px; top: 44px;
    font-size: 13px; letter-spacing: 5px;
  }
  .motto-dot {
    position: absolute; right: 44px; top: 40px;
    width: 24px; height: 24px; border-radius: 50%; background: var(--ink-black);
  }
  .person { position: absolute; left: 48px; top: 112px; }
  .person-name { font-size: 26px; font-weight: 400; line-height: 1.1; }
  .person-role { font-size: 15px; margin-top: 2px; }
  .contact { position: absolute; left: 48px; top: 200px; list-style: none; font-size: 17px; line-height: 1.55; }
  .contact li { display: flex; align-items: center; gap: 8px; }
  .contact svg { width: 13px; height: 13px; fill: var(--text-dark); flex: none; }
  .contact .plain { padding-left: 21px; }
  .address {
    position: absolute; right: 48px; bottom: 36px; text-align: right;
    font-size: 20px; line-height: 1.3; font-style: normal;
  }
</style>
</head>
<body>
<main class="sheet">

  <section class="card card-front" aria-label="Card front">
    <div class="brand">
      <div class="brand-name"><span class="brand-dot"></span>THE CORVELLA SPA</div>
      <p class="brand-tagline">a quiet retreat for every guest</p>
    </div>
    <p class="front-web">www.<span class="accent">thecorvellaspa</span>.com</p>
  </section>

  <section class="card card-back" aria-label="Card back">
    <p class="motto">Breathe deep. Savor Today</p>
    <span class="motto-dot" aria-hidden="true"></span>

    <div class="person">
      <h1 class="person-name">Daniel Marsh</h1>
      <p class="person-role">Executive Manager</p>
    </div>

    <ul class="contact">
      <li>
        <svg viewBox="0 0 24 24" aria-hidden="true"><path d="M6.6 10.8a15.1 15.1 0 0 0 6.6 6.6l2.2-2.2c.3-.3.7-.4 1-.2 1.1.4 2.3.6 3.6.6.6 0 1 .4 1 1V20c0 .6-.4 1-1 1C10.6 21 3 13.4 3 4c0-.6.4-1 1-1h3.5c.6 0 1 .4 1 1 0 1.3.2 2.5.6 3.6.1.3 0 .7-.2 1z"/></svg>
        (518) 462 3085
      </li>
      <li>
        <svg viewBox="0 0 24 24" aria-hidden="true"><path d="M2 5h20v14H2zm2 2v.5l8 5 8-5V7zm0 2.8V17h16V9.8l-8 5z"/></svg>
        info@thecorvellaspa.com
      </li>
      <li>
        <svg viewBox="0 0 24 24" aria-hidden="true"><path d="M12 2a10 10 0 1 0 0 20 10 10 0 0 0 0-20zm6.9 9h-3a15 15 0 0 0-1.3-6 8 8 0 0 1 4.3 6zM12 4.1c.9 1.3 1.7 3.6 1.9 6.9h-3.8c.2-3.3 1-5.6 1.9-6.9zM9.4 5a15 15 0 0 0-1.3 6h-3a8 8 0 0 1 4.3-6zM5.1 13h3a15 15 0 0 0 1.3 6 8 8 0 0 1-4.3-6zm6.9 6.9c-.9-1.3-1.700-3.6-1.9-6.9h3.8c-.2 3.3-1 5.6-1.9 6.9zm2.6-.9a15 15 0 0 0 1.3-6h3a8 8 0 0 1-4.3 6z"/></svg>
        www.thecorvellaspa.com
      </li>
      <li class="plain">www.thecorvellaspa.com</li>
    </ul>

    <address class="address">
      3817 Birch Lane<br>
      Marlow, Vermont 05344
    </address>
  </section>

</main>
</body>
</html>
```